DUN Meridian Safeguard Sell Sheet

We need a two-sided portrait-style sell sheet for a new insurance product called the DUN Meridian Safeguard. The DUN Meridian Safeguard is a custom Executive Risk commercial insurance policy that provides the broadest level of protection available in the marketplace. The sell sheet would primarily use the colors blue, gray and white, have clean lines, minimal graphics (perhaps a picture of an executive boardroom at the top), three boxes (or text areas) to provide a brief description of the specific insurance products provided by the Meridian (Directors & Officers Liability, Employment Practices Liability, and Fiduciary Liability), be easy to read and really pique the reader's interest to learn more about the product. The title (DUN Meridian Safeguard) would overlay the graphic at the top, and just below the title would be the phrase "Expect More", which is our tagline for the product. There would be a two-sentence lead-in phrase just below the graphic ("Meridian Safeguard is an exclusive, custom-designed insurance policy tailored to a company’s specific risk profile. The policy was created to provide clients with a premium, industry-leading level of protection not found in the standard insurance marketplace". There needs to be another text section entitled "Return on Investment" and capable of containing three medium length sentences. There needs to be an "About Us" section (three to four medium-length sentences) and a "Contact Us" section (contact name, phone (x2), e-mail, address). On the back we want to discuss the specific features of the product by section of the policy (General Terms and Conditions, Directors & Officers Liability Insurance, Employment Practices Liability Insurance, Fiduciary Liability Insurance. This would likely be set out in bullet format.

I have attached a few examples found on the web that are similar to my vision for this sell sheet, but none that exactly fit our needs (whether graphically or due to specific layout).

Insurance

Serif

• I have uploaded a sample done in powerpoint. Please disregard the coloring as I did not have time to choose colors. I did not add the "About Us" and "Contact Us" sections on the front page and would like creative ideas on structuring that. On the back page, I think a nice looking table broken down by section of the policy would look nice, and allow us to enter bulleted coverage features for each section. Both graphics in the sample were found on google without watermarks by searching "board room" and "business agreement", respectively.

```html
<!DOCTYPE html>
<html lang="en">
<head>
<meta charset="utf-8">
<title>DUN Meridian Safeguard Sell Sheet</title>
<link rel="stylesheet" href="https://fonts.googleapis.com/css2?family=Raleway:wght@400;500;600;700;800&family=Open+Sans:wght@400;600;700&display=swap">
<style>
:root{
  --blue:#3b6fb9;
  --blue-deep:#2c5a9e;
  --cyan:#2b9fd6;
  --ink:#222428;
  --text:#3a3c40;
  --dark:#2b2c2f;
  --panel:#3d3f44;
  --paper:#ffffff;
  --paper-tint:#f4f5f7;
  --bg:#e6e7e9;
  --rule:#c9ccd2;
}
*{margin:0;padding:0;box-sizing:border-box}
html,body{width:1200px;height:810px;overflow:hidden;background:var(--bg)}
body{position:relative;font-family:"Open Sans",Arial,sans-serif;color:var(--text)}
.sheet{position:absolute;top:45px;width:520px;height:720px;background:var(--paper);overflow:hidden;box-shadow:0 4px 14px rgba(0,0,0,.18)}
.sheet--front{left:40px}
.sheet--back{left:640px}
.abs{position:absolute}

/* front hero */
.hero-photo{left:0;top:0;width:278px;height:572px;background:linear-gradient(160deg,#4a4c51 0%,#2f3034 45%,#5b5d63 75%,#3a3b3f 100%)}
.hero-title{left:24px;top:18px;font-family:"Raleway",sans-serif;font-weight:700;color:#fff;font-size:28px;line-height:27px;letter-spacing:1px;text-transform:uppercase}
.tagline-top{left:26px;top:392px;width:178px;height:33px;background:var(--blue);clip-path:polygon(0 0,100% 0,88% 100%,0 100%)}
.tagline-top span{position:absolute;left:4px;top:-1px;font-family:"Raleway",sans-serif;font-weight:500;font-size:34px;color:#fff;letter-spacing:1px}
.tagline-main{left:24px;top:424px;font-family:"Raleway",sans-serif;font-weight:800;font-size:54px;color:#fff;letter-spacing:1px}
.short-rule{left:28px;top:483px;width:34px;height:2px;background:var(--blue)}
.lead{left:28px;top:490px;width:208px;font-size:8.3px;line-height:11px;color:#e3e4e7;text-align:justify}

.col-right{left:278px;top:0;width:242px;height:572px;background:linear-gradient(#fff 55%,var(--paper-tint))}
.band{position:absolute;height:31px;background:var(--blue);color:#fff;font-family:"Raleway",sans-serif;font-size:14px;display:flex;align-items:center;justify-content:center;gap:6px;box-shadow:0 3px 4px rgba(0,0,0,.18)}
.band b{font-weight:700}
.band::before,.band::after{content:"";width:26px;height:1px;background:#fff}
.band--about{left:264px;top:21px;width:256px}
.band--roi{left:264px;top:118px;width:256px}
.band--products{left:264px;top:214px;width:256px}
.copy{position:absolute;font-size:7.6px;line-height:10.4px;color:var(--text);text-align:justify}

.product{position:absolute;left:250px;width:260px}
.product .icon{position:absolute;left:0;top:0}
.product h3{position:absolute;left:69px;top:0;font-family:"Raleway",sans-serif;font-weight:700;font-size:11.5px;color:var(--ink);white-space:nowrap}
.product h3 span{color:var(--cyan);font-weight:500}
.product p{position:absolute;left:69px;top:16px;width:190px;font-size:7.4px;line-height:10px}
.product .sep{position:absolute;left:69px;top:68px;width:50px;height:1px;background:var(--blue)}

.statement{left:6px;top:572px;width:508px;height:62px;background:var(--blue);color:#fff;font-family:"Raleway",sans-serif;font-weight:700;font-size:12.6px;line-height:16px;text-align:center;text-transform:uppercase;padding-top:7px}
.footer-front{left:0;top:634px;width:520px;height:80px;background:#f7f8fa}
.brand{position:absolute;font-family:"Raleway",sans-serif;font-weight:700;color:var(--blue)}
.brand .big{display:block;font-size:44px;line-height:42px;letter-spacing:3px}
.brand .small{display:block;font-size:9.5px;letter-spacing:.5px;text-transform:uppercase}
.divider{position:absolute;width:1px;background:#555}
.contact{position:absolute;font-size:7.6px;line-height:10.2px}
.contact h4{font-family:"Raleway",sans-serif;font-size:11.5px;color:var(--cyan);font-weight:700}
.contact h4 span{font-weight:400}
.contact h5{font-family:"Raleway",sans-serif;font-size:8.8px;font-weight:800;margin:2px 0 4px;text-transform:uppercase}
.contact li{list-style:none;display:flex;align-items:center;gap:5px}
.contact li i{width:7px;height:7px;border-radius:50%;background:var(--cyan);display:inline-block}
.stripe{position:absolute;left:0;top:714px;width:520px;height:6px;background:var(--blue)}

/* back */
.top-stripe{left:0;top:0;width:330px;height:6px;background:var(--blue)}
.top-stripe--dark{left:338px;width:182px;background:var(--dark)}
.product-image{left:27px;top:40px;width:190px;height:160px;border:1px dashed var(--rule);background:linear-gradient(#f3f4f6,#e7e9ec);border-radius:3px}
.image-caption{left:27px;top:207px;width:190px;text-align:center;font-size:7px;letter-spacing:4px;color:#444}
.band--features{left:241px;top:20px;width:279px}
.band--terms{left:126px;top:236px;width:266px}
.features-intro{left:245px;top:70px;width:256px}
.checks{position:absolute;left:245px;top:114px;width:260px;list-style:none}
.checks li{position:relative;padding-left:17px;font-size:7.6px;line-height:10.2px;margin-bottom:4.2px}
.checks li svg{position:absolute;left:0;top:2px}
.terms-copy{left:27px;top:284px;width:470px;font-size:6.9px;line-height:9.2px}
.section{position:absolute;left:27px;width:470px}
.section .icon{position:absolute;left:4px;top:2px}
.section h3{position:absolute;left:64px;top:0;font-family:"Raleway",sans-serif;font-weight:700;font-size:11.5px;color:var(--ink)}
.section h3 span{color:var(--cyan);font-weight:500}
.section p{position:absolute;left:64px;top:16px;width:404px;font-size:6.6px;line-height:9.1px;text-align:justify}
.footer-back{left:0;top:622px;width:520px;height:92px;background:var(--dark)}
.footer-back .contact{color:#fff}
.footer-back .contact h5{color:#fff}
</style>
</head>
<body>

<section class="sheet sheet--front" aria-label="Front of sell sheet">
  <div class="abs hero-photo" role="img" aria-label="Photo of a smiling executive in a grey suit, arms crossed, before city towers"></div>
  <h1 class="abs hero-title">DUN<br>Meridian<br>Safeguard</h1>

  <div class="abs col-right"></div>
  <div class="band band--about">About <b>Us</b></div>
  <p class="copy" style="left:296px;top:61px;width:212px">Lorem Ipsum is simply dummy text of the printing and typesetting industry. Lorem Ipsum has been the industry's standard dummy text ever since the 1500s.</p>
  <div class="band band--roi">Return on <b>Investment</b></div>
  <p class="copy" style="left:296px;top:160px;width:212px">Lorem Ipsum is simply dummy text of the printing and typesetting industry. Lorem Ipsum has been the industry's standard dummy text ever since the 1500s.</p>
  <div class="band band--products">Insurance <b>Products</b></div>
  <p class="copy" style="left:296px;top:256px;width:212px">Lorem Ipsum is simply dummy text of the printing and typesetting industry. Lorem Ipsum has been the industry's standard dummy text ever since the 1500s, when an unknown printer took a galley of type and scrambled it to make a type specimen book.</p>

  <div class="product" style="top:322px">
    <svg class="icon" width="56" height="56" viewBox="0 0 56 56"><circle cx="28" cy="28" r="27" fill="#fff" stroke="#3b6fb9" stroke-width="2"/><circle cx="28" cy="28" r="22" fill="#3b6fb9"/><circle cx="28" cy="22" r="6" fill="#fff"/><path d="M16 39c1-7 6-10 12-10s11 3 12 10z" fill="#fff"/></svg>
    <h3><span>Directors &amp;</span> Officers Liability</h3>
    <p>Lorem Ipsum is simply dummy text of the printing and typesetting industry.</p>
    <div class="sep"></div>
  </div>
  <div class="product" style="top:408px">
    <svg class="icon" width="56" height="56" viewBox="0 0 56 56"><circle cx="28" cy="28" r="27" fill="#fff" stroke="#3b6fb9" stroke-width="2"/><circle cx="28" cy="28" r="22" fill="#3b6fb9"/><rect x="17" y="18" width="22" height="16" fill="none" stroke="#fff" stroke-width="2"/><polyline points="20,30 25,25 29,28 35,21" fill="none" stroke="#fff" stroke-width="1.8"/><path d="M24 34l-3 6M32 34l3 6" stroke="#fff" stroke-width="1.8"/></svg>
    <h3><span>Employment</span> Practices Liability</h3>
    <p>Lorem Ipsum is simply dummy text of the printing and typesetting industry.</p>
    <div class="sep"></div>
  </div>
  <div class="product" style="top:500px">
    <svg class="icon" width="56" height="56" viewBox="0 0 56 56"><circle cx="28" cy="28" r="27" fill="#fff" stroke="#3b6fb9" stroke-width="2"/><circle cx="28" cy="28" r="22" fill="#3b6fb9"/><path d="M14 26l7-5 6 3 5-3 10 5-3 4-10 6-7-4z" fill="#fff"/></svg>
    <h3><span>Fiduciary</span> Liability</h3>
    <p>Lorem Ipsum is simply dummy text of the printing and typesetting industry.</p>
  </div>

  <div class="abs tagline-top"><span>EXPECT</span></div>
  <div class="abs tagline-main">MORE!</div>
  <div class="abs short-rule"></div>
  <p class="abs lead">Meridian Safeguard is an exclusive, custom-designed insurance policy tailored to a company's specific risk profile. The policy was created to provide clients with a premium, industry-leading level of protection not found in the standard insurance marketplace</p>

  <div class="abs statement">The DUN Meridian Safeguard is a custom executive risk<br>commercial insurance policy that provides the broadest<br>level of protection available in the marketplace.</div>

  <div class="abs footer-front"></div>
  <div class="brand" style="left:32px;top:648px"><span class="big">DUN</span><span class="small">Meridian Safeguard</span></div>
  <div class="divider" style="left:259px;top:644px;height:60px"></div>
  <div class="contact" style="left:354px;top:641px">
    <h4>CONTACT <span>US</span></h4>
    <h5>Contact name goes here</h5>
    <ul>
      <li><i></i>Address Goes Here</li>
      <li><i></i>0123 456 789</li>
      <li><i></i>info@dunmeridian.com</li>
      <li><i></i>www.dunmeridian.com</li>
    </ul>
  </div>
  <div class="stripe"></div>
</section>

<section class="sheet sheet--back" aria-label="Back of sell sheet">
  <div class="abs top-stripe"></div>
  <div class="abs top-stripe top-stripe--dark"></div>

  <div class="abs product-image" role="img" aria-label="Product image placeholder"></div>
  <div class="abs image-caption">PRODUCT IMAGE</div>

  <div class="band band--features">Features</div>
  <p class="copy features-intro">Lorem Ipsum is simply dummy text of the printing and typesetting industry. Lorem Ipsum has been the industry's standard dummy text ever since the 1500s.</p>
  <ul class="checks">
    <li><svg width="9" height="9" viewBox="0 0 10 10"><circle cx="5" cy="5" r="5" fill="#3b6fb9"/><path d="M2.6 5.2l1.6 1.6 3.2-3.4" fill="none" stroke="#fff" stroke-width="1.3"/></svg>Lorem Ipsum is simply dummy text of the printing and typesetting industry.</li>
    <li><svg width="9" height="9" viewBox="0 0 10 10"><circle cx="5" cy="5" r="5" fill="#3b6fb9"/><path d="M2.6 5.2l1.6 1.6 3.2-3.4" fill="none" stroke="#fff" stroke-width="1.3"/></svg>Lorem Ipsum is simply dummy text of the printing and typesetting industry.</li>
    <li><svg width="9" height="9" viewBox="0 0 10 10"><circle cx="5" cy="5" r="5" fill="#3b6fb9"/><path d="M2.6 5.2l1.6 1.6 3.2-3.4" fill="none" stroke="#fff" stroke-width="1.3"/></svg>Lorem Ipsum is simply dummy text of the printing and typesetting industry.</li>
    <li><svg width="9" height="9" viewBox="0 0 10 10"><circle cx="5" cy="5" r="5" fill="#3b6fb9"/><path d="M2.6 5.2l1.6 1.6 3.2-3.4" fill="none" stroke="#fff" stroke-width="1.3"/></svg>Lorem Ipsum is simply dummy text of the printing and typesetting industry.</li>
  </ul>

  <div class="band band--terms">General <b>Terms &amp; Conditions</b></div>
  <p class="copy terms-copy">Lorem Ipsum is simply dummy text of the printing and typesetting industry. Lorem Ipsum has been the industry's standard dummy text ever since the 1500s, when an unknown printer took a galley of type and scrambled it to make a type specimen book. Lorem Ipsum is simply dummy text of the printing and typesetting industry. Lorem Ipsum has been the industry's standard dummy text ever since the 1500s, when an unknown printer took a galley of type and scrambled it to make a type specimen book.</p>

  <div class="section" style="top:328px">
    <svg class="icon" width="42" height="42" viewBox="0 0 42 42"><circle cx="21" cy="21" r="20" fill="#3b6fb9" stroke="#fff" stroke-width="2"/><circle cx="21" cy="16" r="5" fill="#fff"/><path d="M11 31c1-6 5-8 10-8s9 2 10 8z" fill="#fff"/></svg>
    <h3><span>Directors &amp;</span> Officers Liability</h3>
    <p>Lorem Ipsum is simply dummy text of the printing and typesetting industry. Lorem Ipsum is simply dummy text of the printing and typesetting industry. Lorem Ipsum is simply dummy text of the printing and typesetting industry. Lorem Ipsum is simply dummy text of the printing and typesetting industry. Lorem Ipsum is simply dummy text of the printing and typesetting industry. Lorem Ipsum is simply dummy text of the printing and typesetting industry. Lorem Ipsum is simply dummy text of the printing and typesetting industry. Lorem Ipsum is simply dummy text of the printing and typesetting industry. Lorem Ipsum is simply dummy text of the printing and typesetting industry.</p>
  </div>
  <div class="section" style="top:427px">
    <svg class="icon" width="42" height="42" viewBox="0 0 42 42"><circle cx="21" cy="21" r="20" fill="#3b6fb9" stroke="#fff" stroke-width="2"/><rect x="12" y="12" width="18" height="13" fill="none" stroke="#fff" stroke-width="1.8"/><polyline points="14,22 18,18 21,20 27,15" fill="none" stroke="#fff" stroke-width="1.5"/><path d="M18 25l-3 5M24 25l3 5" stroke="#fff" stroke-width="1.5"/></svg>
    <h3><span>Employment</span> Practices Liability</h3>
    <p>Lorem Ipsum is simply dummy text of the printing and typesetting industry. Lorem Ipsum is simply dummy text of the printing and typesetting industry. Lorem Ipsum is simply dummy text of the printing and typesetting industry. Lorem Ipsum is simply dummy text of the printing and typesetting industry. Lorem Ipsum is simply dummy text of the printing and typesetting industry. Lorem Ipsum is simply dummy text of the printing and typesetting industry. Lorem Ipsum is simply dummy text of the printing and typesetting industry. Lorem Ipsum is simply dummy text of the printing and typesetting industry.</p>
  </div>
  <div class="section" style="top:526px">
    <svg class="icon" width="42" height="42" viewBox="0 0 42 42"><circle cx="21" cy="21" r="20" fill="#3b6fb9" stroke="#fff" stroke-width="2"/><path d="M10 19l6-4 5 2 4-2 8 4-2 3-8 5-6-3z" fill="#fff"/></svg>
    <h3><span>Fiduciary</span> Liability</h3>
    <p>Lorem Ipsum is simply dummy text of the printing and typesetting industry. Lorem Ipsum is simply dummy text of the printing and typesetting industry. Lorem Ipsum is simply dummy text of the printing and typesetting industry. Lorem Ipsum is simply dummy text of the printing and typesetting industry. Lorem Ipsum is simply dummy text of the printing and typesetting industry. Lorem Ipsum is simply dummy text of the printing and typesetting industry. Lorem Ipsum is simply dummy text of the printing and typesetting industry. Lorem Ipsum is simply dummy text of the printing and typesetting industry.</p>
  </div>

  <div class="abs footer-back"></div>
  <div class="brand" style="left:32px;top:645px"><span class="big">DUN</span><span class="small">Meridian Safeguard</span></div>
  <div class="divider" style="left:258px;top:638px;height:60px;background:#777"></div>
  <div class="contact" style="left:354px;top:640px">
    <h4>CONTACT</h4>
    <h5>Contact name goes here</h5>
    <ul>
      <li><i></i>Address Goes Here</li>
      <li><i></i>0123 456 789</li>
      <li><i></i>info@dunmeridian.com</li>
      <li><i></i>www.dunmeridian.com</li>
    </ul>
  </div>
  <div class="stripe"></div>
</section>

</body>
</html>
```